Business card and stationary for eco-aware technology company
Verdalux: Green-minded Scrap Recovery
Business card and stationary for eco-aware technology company - Chemicals
Creative Brief
Professional
Tam Brendow
Managing Director
7-3, 2nd Floor, Pelham Court, Quarry Road, 10450 Georgetown, Penang, Malaysia
+604-8XXXXXX
+6011-5274 XXXX
xxx@verdalux.example
http://www.verdalux.example
YYYYYYY-K
Hello, My name is Tam Brendow, and I am MD of Verdalux. I would like a letterhead and a business card for myself. Verdalux is a Malaysia-based startup with a focus on developing technology for urban mining ( http://scrapharvest.example/ ). Verdalux's name is legally Verdalux Sdn. Bhd., but maybe the shorter form, 'Verdalux' looks better on a business card. Perhaps the "Sdn. Bhd." could be hidden in there somewhere. Up to you! For the business card, the following info should be used: Tam Brendow Managing Director MChem, Ph.D (Chemistry) The back side of the business card can be blank, or it can be very simply decorated. I am on Malaysian time (GMT +8) so please forgive me if my feedback appears delayed. Thanks & good luck, - Tam
Empty is fine. Very simple decoration if you want - maybe just the company logo in the center.
tbrendow tbrendow
Hey, Sorry for the slow feedback. I've just got back to the office. Firstly, I am happy to review the business card designs on this site. However, the stationary designs are too big to preview and quorbasketch's site makes it too slow for me to look at the designs. So, would you designers be able to host the images on a web server, or put them in a .zip file? Private message me the URL and I'll download them and use an image viewer to see them offline. Sorry for the extra work - blame QS's crap design. Ok, now for some feedback: 1) The dark 'Eco' green does not look nice on the card. Please use only a little bit! 2) Lighter greens are nice. Like the colour of the 3 leaves. 3) No transparent cards, please. 4) The back of the card should have a very simple design. Maybe just the 3 leaves on a white background, with no text? 5) I love the designs with the big leaf (#191). It's clever. I also love the designs with the circuit pattern (#212, #213, #214). That's clever too. Private message me if you want more feedback or ideas. I'll try to reply fast. Thanks, - Tam

```html
<!DOCTYPE html>
<html lang="en">
<head>
<meta charset="utf-8">
<title>Verdalux business card</title>
<link href="https://fonts.googleapis.com/css2?family=Open+Sans:wght@400;600;700&family=Roboto:wght@400;500;700&display=swap" rel="stylesheet">
<style>
  :root {
    --bg: #e9ebe6;
    --green-dark: #1f6b2a;
    --green-deep: #16551f;
    --green-mid: #3f9a2f;
    --green-light: #7cc242;
    --ink: #2f3a2f;
    --muted: #5d6a5d;
    --white: #ffffff;
    --rule: #9aa59a;
  }
  * { box-sizing: border-box; margin: 0; padding: 0; }
  html, body { width: 1200px; height: 901px; overflow: hidden; }
  body {
    background: var(--bg);
    font-family: "Open Sans", Arial, sans-serif;
    color: var(--ink);
    position: relative;
  }
  .card {
    position: absolute;
    left: 250px;
    width: 700px;
    height: 400px;
    border-radius: 22px;
    overflow: hidden;
    box-shadow: 0 8px 24px rgba(0,0,0,.18);
  }
  /* back side */
  .card-back { top: 36px; }
  .card-back .leaf-field {
    position: absolute; inset: 0;
    background: radial-gradient(circle at 50% 45%, #3b8f34 0%, var(--green-dark) 55%, var(--green-deep) 100%);
  }
  .card-back .brand-mark {
    position: absolute; top: 150px; left: 0; right: 0;
    text-align: center;
    font-family: "Roboto", Arial, sans-serif;
    font-weight: 700;
    font-size: 54px;
    color: var(--green-light);
    letter-spacing: 1px;
  }
  .card-back .web-line {
    position: absolute; bottom: 48px; left: 0; right: 0;
    display: flex; align-items: center; justify-content: center; gap: 16px;
    color: #d6ecc8; font-size: 17px; letter-spacing: 1px;
  }
  .card-back .web-line span.rule { display: block; width: 200px; height: 1px; background: #9fcf86; }

  /* front side */
  .card-front { top: 466px; background: var(--white); }
  .side-bar {
    position: absolute; left: 0; top: 62px; width: 10px; height: 56px;
    background: var(--green-dark);
  }
  .person { position: absolute; left: 30px; top: 56px; }
  .person .name {
    font-family: "Roboto", Arial, sans-serif;
    font-size: 26px; font-weight: 500; color: var(--green-dark);
  }
  .person .creds { font-size: 17px; font-weight: 400; color: var(--green-mid); }
  .person .role { font-size: 17px; color: var(--muted); margin-top: 2px; }
  .contacts { position: absolute; left: 30px; top: 142px; list-style: none; }
  .contacts li {
    display: flex; align-items: center; gap: 10px;
    font-size: 15px; color: var(--muted); height: 25px;
  }
  .contacts svg { width: 14px; height: 14px; fill: var(--green-mid); }
  .brand { position: absolute; right: 36px; top: 80px; text-align: left; }
  .brand .wordmark {
    display: flex; align-items: center; gap: 12px;
  }
  .brand .dot { width: 44px; height: 44px; border-radius: 50%; background: var(--green-light); }
  .brand .name {
    font-family: "Roboto", Arial, sans-serif;
    font-size: 52px; font-weight: 700; color: var(--green-mid); line-height: 1;
  }
  .brand .tagline {
    font-size: 12px; font-weight: 600; letter-spacing: 2px; color: var(--green-dark);
    text-transform: uppercase; margin-top: 4px; text-align: right;
  }
  .company-info { position: absolute; right: 40px; top: 262px; width: 330px; text-align: right; }
  .company-info .divider { height: 1px; background: var(--rule); margin-bottom: 12px; }
  .company-info p { font-size: 14px; color: var(--muted); line-height: 21px; }
</style>
</head>
<body>
  <section class="card card-back">
    <div class="leaf-field" role="img" aria-label="Dark green background with a faint leaf pattern"></div>
    <div class="brand-mark">Verdalux</div>
    <div class="web-line"><span class="rule"></span>www.verdalux.example<span class="rule"></span></div>
  </section>

  <section class="card card-front">
    <div class="side-bar"></div>
    <div class="person">
      <div class="name">Tam Brendow, <span class="creds">MChem, Ph.D (Chemistry)</span></div>
      <div class="role">Managing Director</div>
    </div>
    <ul class="contacts">
      <li><svg viewBox="0 0 16 16"><path d="M3 1h3l1.5 4-2 1.2a9 9 0 0 0 4.3 4.3l1.2-2L15 10v3a2 2 0 0 1-2 2A12 12 0 0 1 1 3a2 2 0 0 1 2-2z"/></svg>+604-8XXXXXX</li>
      <li><svg viewBox="0 0 16 16"><path d="M4 0h8a1 1 0 0 1 1 1v14a1 1 0 0 1-1 1H4a1 1 0 0 1-1-1V1a1 1 0 0 1 1-1zm1 2v10h6V2z"/></svg>+6011-5274 XXXX</li>
      <li><svg viewBox="0 0 16 16"><path d="M4 1h7l2 2v3H4zM1 7h14v6h-2v2H3v-2H1zm4 4v3h6v-3z"/></svg>+604-8YYYYYY</li>
      <li><svg viewBox="0 0 16 16"><path d="M1 3h14v10H1zm1.5 1.5L8 9l5.5-4.5z"/></svg>xxx@verdalux.example</li>
      <li><svg viewBox="0 0 16 16"><path d="M8 0a8 8 0 1 0 0 16A8 8 0 0 0 8 0zm0 2a6 6 0 0 1 5.7 4H2.3A6 6 0 0 1 8 2zM2.3 10h11.4A6 6 0 0 1 2.3 10z"/></svg>www.verdalux.example</li>
    </ul>
    <div class="brand">
      <div class="wordmark"><span class="dot"></span><span class="name">Verdalux</span></div>
      <div class="tagline">Green-minded Scrap Recovery</div>
    </div>
    <div class="company-info">
      <div class="divider"></div>
      <p>License No YYYYYYY-K</p>
      <p>7-3, 2nd Floor, Pelham Court, Quarry Road</p>
      <p>10450 Georgetown, Penang, Malaysia</p>
    </div>
  </section>
</body>
</html>
```